Brantley Advisory Group provides support for renewable energy projects to utilities and suppliers

I need a professional looking business card that is both simple and elegant and unique. My clients are mostly large organizations not individuals. I am a consultant with my own company that is small but would like to give clients the impression I am larger. Smart grid, fiber optics, software, field hardware, distribution automation, substation automation, operations, energy storage/batteries, microgrids, customer service, strategy/roadmaps, conservation, Automated Metering Infrastruture (AMI or smart meters) are all areas of focus.

Target Market(s)

Utilities, suppliers, governmental agencies involved in energy. All types of energy especially natural gas and electrical. Especially renewable energy or green projects.

Contact Information for Business Card

Name - Corvin Ashdale Cell Phone - 425.318.2746 Email - cashdale@brantleyag-example.com
Company - Brantley Advisory Group (logo) Title - Principal

Font styles to use
Serif
Sans Serif

Colors

Designer to choose colors to be used in the design.

Requirements
Must have
• Simple and professional and powerful.
• Unique/creative design.
Nice to have
• Utilize color scheme to accent logo colors. Maybe some geometric pattern on edge of card with color.
Should not have
• Busy, complicated, traditional

```html
<!DOCTYPE html>
<html lang="en">
<head>
<meta charset="UTF-8">
<title>Brantley Advisory Group — Business Card</title>
<link rel="stylesheet" href="https://fonts.googleapis.com/css2?family=Poppins:wght@400;500;700;800&display=swap">
<style>
  :root {
    --stage: #2a2a2c;
    --card-white: #ffffff;
    --card-blue: #1f45a3;
    --brand-blue: #2b3a9c;
    --brand-green: #5f9a3a;
    --text-white: #ffffff;
    --card-shadow: 0 14px 34px rgba(0, 0, 0, 0.45);
  }
  * { margin: 0; padding: 0; box-sizing: border-box; }
  html, body {
    width: 1200px;
    height: 900px;
    overflow: hidden;
    background: var(--stage);
    font-family: "Poppins", sans-serif;
  }
  .canvas {
    width: 1200px;
    height: 900px;
    display: flex;
    flex-direction: column;
    align-items: center;
    justify-content: center;
    gap: 56px;
  }
  .card {
    position: relative;
    width: 630px;
    height: 360px;
    box-shadow: var(--card-shadow);
    overflow: hidden;
  }

  /* Front */
  .card--front { background: var(--card-white); }
  .edge-accent {
    position: absolute;
    left: 0;
    width: 10px;
    height: 44px;
  }
  .edge-accent--blue { top: 30px; background: var(--brand-blue); }
  .edge-accent--green { top: 186px; background: var(--brand-green); }

  .identity {
    position: absolute;
    left: 44px;
    top: 30px;
  }
  .identity__name {
    font-weight: 800;
    font-size: 26px;
    letter-spacing: 0.5px;
    color: var(--brand-blue);
    text-transform: uppercase;
    line-height: 1.1;
  }
  .identity__title {
    font-weight: 500;
    font-size: 19px;
    color: var(--brand-green);
    line-height: 1.2;
  }

  .contact {
    position: absolute;
    left: 44px;
    top: 188px;
    list-style: none;
  }
  .contact__item {
    display: flex;
    align-items: center;
    gap: 12px;
    font-size: 16px;
    color: var(--brand-blue);
    line-height: 1.7;
  }
  .contact__icon { width: 16px; height: 16px; flex: none; }

  .wordmark {
    position: absolute;
    display: flex;
    align-items: center;
    gap: 12px;
  }
  .wordmark__square {
    width: 30px;
    height: 30px;
    flex: none;
  }
  .wordmark__name {
    font-weight: 700;
    line-height: 1.1;
    white-space: nowrap;
  }
  .card--front .wordmark { right: 40px; bottom: 40px; }
  .card--front .wordmark__square { background: var(--brand-green); }
  .card--front .wordmark__name { font-size: 24px; color: var(--brand-blue); }

  /* Back */
  .card--back { background: var(--card-blue); }
  .card--back .wordmark {
    left: 50%;
    top: 50%;
    transform: translate(-50%, -50%);
    gap: 16px;
  }
  .card--back .wordmark__square { width: 38px; height: 38px; background: var(--text-white); }
  .card--back .wordmark__name { font-size: 32px; color: var(--text-white); }
</style>
</head>
<body>
<main class="canvas">
  <section class="card card--front" aria-label="Business card front">
    <span class="edge-accent edge-accent--blue"></span>
    <span class="edge-accent edge-accent--green"></span>

    <div class="identity">
      <h1 class="identity__name">Corvin Ashdale</h1>
      <p class="identity__title">Principal</p>
    </div>

    <ul class="contact">
      <li class="contact__item">
        <svg class="contact__icon" viewBox="0 0 24 24" aria-hidden="true">
          <path fill="#5f9a3a" d="M6.6 10.8a15.1 15.1 0 0 0 6.6 6.6l2.2-2.2a1 1 0 0 1 1-.25 11.4 11.4 0 0 0 3.6.57 1 1 0 0 1 1 1V20a1 1 0 0 1-1 1A17 17 0 0 1 3 4a1 1 0 0 1 1-1h3.5a1 1 0 0 1 1 1c0 1.25.2 2.45.57 3.57a1 1 0 0 1-.25 1z"/>
        </svg>
        <span>425.318.2746</span>
      </li>
      <li class="contact__item">
        <svg class="contact__icon" viewBox="0 0 24 24" aria-hidden="true">
          <rect x="2" y="5" width="20" height="14" fill="#5f9a3a"/>
          <path d="M2 5l10 8 10-8" fill="none" stroke="#ffffff" stroke-width="1.6"/>
        </svg>
        <span>cashdale@brantleyag-example.com</span>
      </li>
    </ul>

    <div class="wordmark">
      <span class="wordmark__square"></span>
      <span class="wordmark__name">Brantley Advisory Group</span>
    </div>
  </section>

  <section class="card card--back" aria-label="Business card back">
    <div class="wordmark">
      <span class="wordmark__square"></span>
      <span class="wordmark__name">Brantley Advisory Group</span>
    </div>
  </section>
</main>
</body>
</html>
```